Business Card Design

We need a business card design that can also be aplied for postcards. We are a small indie record company that also do consulting, and development of independat artitst . I already have the name and the basic idea of what i am looking for but i am open to any suggestion.
Info for the card
Name of the company : Velmora Records
NAME : Tobias Lindqvist
PHONE : 314-5820641
EMAIL : hello@velmorarecords.example
WEB: www.velmorarecords.example
Target Market(s)
Male - Female independent musicians ages 18 to 45
Industry/Entity Type
Record Company
Contact Information for Business Card
Independant records company that also works in consulting for music business models for independent artists
Look and feel

```html
<!DOCTYPE html>
<html lang="en">
<head>
<meta charset="utf-8">
<title>Velmora Records – Business Card</title>
<link rel="stylesheet" href="https://fonts.googleapis.com/css2?family=Marcellus+SC&family=Andika&display=swap">
<style>
  :root {
    --paper: #ffffff;
    --wine: #800000;
    --rose: #d33a62;
    --ink-light: #ffffff;
    --shadow: #2a0000;
  }
  html, body {
    margin: 0;
    padding: 0;
    width: 1200px;
    height: 702px;
    overflow: hidden;
    background: var(--paper);
  }
  .canvas {
    position: relative;
    width: 1200px;
    height: 702px;
    background: var(--paper);
  }
  .card {
    position: absolute;
    left: 46px;
    top: 43px;
    width: 1106px;
    height: 616px;
    background: var(--wine);
    overflow: hidden;
  }
  .side-band {
    position: absolute;
    left: 0;
    top: 0;
    width: 138px;
    height: 100%;
    background: var(--rose);
  }
  .disc {
    position: absolute;
    left: 0;
    top: 0;
    width: 1106px;
    height: 616px;
  }
  .company-name {
    position: absolute;
    left: 609px;
    top: 54px;
    transform: translateX(-50%);
    margin: 0;
    font-family: "Marcellus SC", serif;
    font-weight: 400;
    font-size: 104px;
    line-height: 1;
    white-space: nowrap;
    color: var(--ink-light);
    text-shadow: 4px 4px 3px var(--shadow);
  }
  .contact {
    position: absolute;
    left: 475px;
    top: 0;
    margin: 0;
    font-family: "Andika", sans-serif;
    color: var(--ink-light);
  }
  .contact-name {
    position: absolute;
    left: 0;
    top: 270px;
    font-size: 31px;
    line-height: 1;
    white-space: nowrap;
  }
  .contact-line {
    position: absolute;
    left: 0;
    font-size: 32px;
    line-height: 1;
    white-space: nowrap;
  }
  .contact-line .label {
    font-size: 26px;
  }
  .contact-line.phone { top: 343px; }
  .contact-line.email { top: 407px; }
  .contact-line.web   { top: 472px; }
</style>
</head>
<body>
<div class="canvas">
  <section class="card">
    <div class="side-band"></div>
    <svg class="disc" viewBox="0 0 1106 616" aria-hidden="true">
      <circle cx="139" cy="402" r="118" fill="var(--rose)" stroke="var(--wine)" stroke-width="3"/>
      <circle cx="139" cy="402" r="21" fill="var(--wine)"/>
    </svg>
    <h1 class="company-name">Velmora Records</h1>
    <div class="contact">
      <p class="contact-name">Tobias Lindqvist</p>
      <p class="contact-line phone"><span class="label">PHONE &nbsp;: </span>314-5820641</p>
      <p class="contact-line email"><span class="label">EMAIL : </span>hello@velmorarecords.example</p>
      <p class="contact-line web"><span class="label">WEB &nbsp;: </span>www.velmorarecords.example</p>
    </div>
  </section>
</div>
</body>
</html>
```